Creative, fresh business card design for Orrin Linings

We need a fresh, creative business card design for Orrin Linings. We are the manufacturer of Orrin Linings in Australia. Wall panels are 2400 x 1200mm panels made from MDF and feature 3D patterns on the face of the panel. The colours to be used are green, silver/grey and white RGB
Red 187
Green 207
Blue 65.

An idea is to possibly use a watermark of one of our designs as a background (like on the "Ferns" design on the left hand side of page 2 of our brochure).

Target Market(s)

Interior designers, architects, builders and home renovators

Industry/Entity Type

Business

Contact Information for Business Card

Details to go on the card are:
Our logo (attached),
Slogan: "Decorative panels for interiors and exteriors",
Contact name,
Position,
Mobile phone number,
Business address,
Business phone,
Business fax,
Website and
Email address.

I have attached a few images of our panels and our brochure for reference.

The colours of the business card should feature our logo colours which are: RGB
Red 187
Green 207
Blue 65

Requirements
Must have
• Very modern fonts and design. Some of the designs shown especially the "Weave" design which is a popular design.
Nice to have
• Creative but simple design. Very contemporary.
Should not have
• Anything ornate or old fashioned.

```html
<!DOCTYPE html>
<html lang="en">
<head>
<meta charset="utf-8">
<title>Orrin Linings – Business Card</title>
<link href="https://fonts.googleapis.com/css2?family=Source+Sans+3:wght@400;600;700&display=swap" rel="stylesheet">
<style>
  :root {
    --brand-green: rgb(187, 207, 65);
    --brand-grey: #8e8f93;
    --grey-dark: #7f8084;
    --label-grey: #9a9b9e;
    --ink: #1f1f1f;
    --white: #ffffff;
    --stage: #000000;
    --pearl-1: #fbfbfb;
    --pearl-2: #eeeeef;
  }
  * { margin: 0; padding: 0; box-sizing: border-box; }
  html, body { width: 1200px; height: 900px; overflow: hidden; background: var(--stage); }
  body { font-family: "Source Sans 3", "Myriad Pro", sans-serif; position: relative; }

  .card {
    position: absolute;
    top: 192px;
    width: 302px;
    height: 491px;
    border-radius: 12px;
    overflow: hidden;
  }
  .card--front { left: 295px; background: var(--white); }
  .card--back { left: 622px; }

  /* front: brand header */
  .brand-header {
    position: absolute; left: 0; top: 0; width: 100%; height: 193px;
    display: flex; align-items: center; justify-content: center; gap: 12px;
  }
  .brand-mark { width: 30px; height: 30px; background: var(--brand-green); }
  .brand-name { font-size: 31px; font-weight: 600; color: var(--brand-grey); letter-spacing: -0.3px; }

  /* front: details panel */
  .details-panel {
    position: absolute; left: 0; top: 193px; width: 100%; height: 298px;
    background: linear-gradient(160deg, #9a9b9f 0%, #8a8b8f 45%, #95969a 100%);
  }
  .contact-name {
    position: absolute; left: 37px; top: 10px;
    font-size: 27px; font-weight: 700; color: var(--brand-green); letter-spacing: 0.2px;
  }
  .contact-role {
    position: absolute; left: 37px; top: 43px;
    font-size: 16px; color: var(--white);
  }
  .contact-list {
    position: absolute; left: 37px; top: 75px; list-style: none;
  }
  .contact-list li {
    display: flex; align-items: center; gap: 6px;
    height: 20.4px; font-size: 14px; color: var(--white);
  }
  .contact-list svg { width: 11px; height: 11px; fill: var(--brand-green); flex: none; }
  .contact-address {
    position: absolute; left: 38px; top: 186px;
    font-size: 14px; line-height: 19px; color: var(--white);
  }
  .slogan-band {
    position: absolute; left: 0; top: 228px; width: 100%; height: 35px;
    background: var(--brand-green);
    display: flex; align-items: center; justify-content: center;
    font-size: 14px; color: var(--ink);
  }

  /* back */
  .back-surface {
    position: absolute; inset: 0;
    background: radial-gradient(ellipse at 50% 45%, var(--pearl-1) 0%, var(--pearl-2) 100%);
  }
  .back-brand {
    position: absolute; left: 0; top: 240px; width: 100%;
    display: flex; align-items: center; justify-content: center; gap: 12px;
  }
  .back-tagline {
    position: absolute; left: 0; top: 298px; width: 100%;
    text-align: center; font-size: 14px; line-height: 17px;
    letter-spacing: 2.6px; color: var(--label-grey);
  }
</style>
</head>
<body>

<section class="card card--front" aria-label="Business card front">
  <header class="brand-header">
    <span class="brand-mark"></span>
    <span class="brand-name">Orrin Linings</span>
  </header>

  <div class="details-panel" role="img" aria-label="Grey panel with faint faceted 3D wall pattern">
    <h1 class="contact-name">Mara Quill</h1>
    <p class="contact-role">Director</p>
    <ul class="contact-list">
      <li><svg viewBox="0 0 12 12"><path d="M3 0h6a1 1 0 0 1 1 1v10a1 1 0 0 1-1 1H3a1 1 0 0 1-1-1V1a1 1 0 0 1 1-1zm0 1.5v8h6v-8zM5.3 10.2h1.4v.8H5.3z"/></svg>712-5550-000</li>
      <li><svg viewBox="0 0 12 12"><path d="M1 4c0-2 10-2 10 0v1H8.5V3.8c-1.5-.6-3.5-.6-5 0V5H1zm2 2h6l1.5 5h-9z"/></svg>717-(555)-010</li>
      <li><svg viewBox="0 0 12 12"><path d="M3 0h5v3H3zM1 4h10v8H1zm2 2v1.5h2V6zm3 0v1.5h2V6zM3 8.5V10h2V8.5zm3 0V10h2V8.5z"/></svg>717-(555)-010</li>
      <li><svg viewBox="0 0 12 12"><path d="M0 2h12v8H0zm1 1.2V9h10V3.2L6 6.6z"/></svg>info@orrinlinings.com</li>
      <li><svg viewBox="0 0 12 12"><circle cx="6" cy="6" r="6"/></svg>www.orrinlinings.com</li>
    </ul>
    <p class="contact-address">14 Kiln Street,<br>Geelong VIC 3220</p>
    <div class="slogan-band">Decorative panels for interiors and exteriors</div>
  </div>
</section>

<section class="card card--back" aria-label="Business card back">
  <div class="back-surface" role="img" aria-label="White faceted 3D wall panel pattern"></div>
  <div class="back-brand">
    <span class="brand-mark"></span>
    <span class="brand-name">Orrin Linings</span>
  </div>
  <p class="back-tagline">decorative panels for<br>interiors &amp; landscapes</p>
</section>

</body>
</html>
```